Ferncastle Financial - Website Design

We need a website design for a new commercial real estate company called Ferncastle Financial. We're effectively commercial mortgage brokers connecting real estate investors to lenders. We need a website that is simple (not busy), elegant, professional, and user-friendly. A lot of the users will be in their 50's and less tech savvy, so a stream-lined design is best. The website will serve as a portal for lenders to review new financing opportunities, as well as for real estate investors to review terms from lenders.
Updates
Just uploaded our logo.
Target Market(s)
Commercial real estate investors and lenders
Industry/Entity Type
Real Estate
Number of Pages Required
1 page
Colors
Designer to choose colors to be used in the design.
Look and feel

```html
<!DOCTYPE html>
<html lang="en">
<head>
<meta charset="utf-8">
<title>Ferncastle Financial</title>
<link rel="stylesheet" href="https://fonts.googleapis.com/css2?family=Roboto:wght@400;500;700&family=Open+Sans:wght@400;600;700&display=swap">
<style>
:root{
  --gold:#c9a063;
  --gold-dark:#b98d4c;
  --navy:#2f4566;
  --navy-deep:#24364f;
  --ink:#222222;
  --text:#555555;
  --muted:#888888;
  --line:#d9d9d9;
  --bg-soft:#f2f2f2;
  --footer:#1f1f1f;
  --white:#ffffff;
}
*{box-sizing:border-box;margin:0;padding:0}
html,body{width:1200px;height:3000px;overflow:hidden}
body{font-family:"Open Sans",Arial,sans-serif;color:var(--text);background:var(--white);position:relative}
h1,h2,h3,h4{font-family:"Roboto",Arial,sans-serif}
.abs{position:absolute}

/* hero */
.hero{position:absolute;left:0;top:0;width:1200px;height:560px;overflow:hidden}
.hero-photo{position:absolute;inset:0;background:linear-gradient(100deg,#6d88b4 0%,#9bb0cf 20%,#3e4656 45%,#7b8797 60%,#c7ced9 78%,#6c7f9c 100%)}
.hero-shade{position:absolute;inset:0;background:rgba(20,28,42,.35)}
.brand{position:absolute;left:98px;top:26px;display:flex;align-items:center;gap:14px;color:var(--white)}
.brand-mark{width:64px;height:64px;border-radius:50%;background:var(--white)}
.brand-name{font-family:"Roboto",sans-serif;font-size:34px;font-weight:500;letter-spacing:1px;line-height:1}
.topbar{position:absolute;right:100px;top:16px;display:flex;align-items:center;gap:24px;color:var(--white);font-size:15px;font-weight:600}
.topbar .phone-num{font-size:19px;font-weight:700}
.topbar svg{vertical-align:-3px;margin-right:8px}
.btn-outline{border:2px solid var(--white);border-radius:24px;color:var(--white);font-weight:700;text-transform:uppercase;display:inline-flex;align-items:center;justify-content:center}
.apply-top{height:38px;padding:0 20px;font-size:14px;gap:6px}
.nav{position:absolute;right:98px;top:70px;display:flex;gap:28px;font-family:"Roboto",sans-serif;font-size:16px;font-weight:500;color:var(--white)}
.nav .active{color:var(--gold)}
.hero-title{position:absolute;left:0;width:1200px;top:150px;text-align:center;color:var(--white);font-size:42px;font-weight:700}
.hero-sub{position:absolute;left:340px;width:520px;top:214px;text-align:center;color:var(--white);font-size:22px;font-weight:600;line-height:32px}
.quote-btn{position:absolute;left:507px;top:302px;width:186px;height:50px;font-size:16px}
.dots{position:absolute;left:568px;top:410px;display:flex;gap:6px}
.dots span{width:12px;height:12px;border-radius:50%;border:2px solid var(--white)}
.dots span.on{background:var(--white)}
.hero-curve{position:absolute;left:0;top:460px}

/* services */
.services{position:absolute;left:98px;top:588px;display:flex;gap:24px}
.service{width:234px;height:252px;border:2px solid var(--line);text-align:center;padding-top:26px}
.service-icon{width:100px;height:100px;border-radius:50%;background:var(--bg-soft);margin:0 auto;display:flex;align-items:center;justify-content:center}
.service h3{font-size:19px;font-weight:500;color:var(--ink);margin-top:30px}
.service p{font-size:13px;line-height:22px;color:var(--muted);margin:10px 18px 0}

/* login */
.logins{position:absolute;left:0;top:924px;width:1200px;height:322px;display:flex}
.login{width:600px;height:322px;position:relative}
.login-client{background:linear-gradient(90deg,#2b3e5b,#3c5274)}
.login-lender{background:linear-gradient(90deg,#d3ab6c,#c9a063)}
.login-icon{position:absolute;left:100px;top:46px}
.login-lender .login-icon{left:650px;left:50px}
.login h2{position:absolute;left:122px;top:62px;color:var(--white);font-size:31px;font-weight:500}
.field{position:absolute;left:122px;width:346px;height:38px;background:var(--white);font-size:14px;color:var(--muted);display:flex;align-items:center;padding-left:14px;gap:8px}
.field-email{top:120px}
.field-pass{top:166px}
.login-submit{position:absolute;left:122px;top:218px;width:114px;height:46px;font-size:15px}
.forgot{position:absolute;left:366px;top:218px;font-size:12px;color:var(--white);text-decoration:underline;font-weight:600}
.login-lender .login-icon{left:650px}

/* blog */
.section-title{position:absolute;left:0;width:1200px;text-align:center;font-size:28px;font-weight:500;color:var(--ink)}
.blog-title{top:1312px}
.post{position:absolute;top:1388px;width:312px}
.post-photo{width:312px;height:212px}
.photo-a{background:linear-gradient(135deg,#dfe4ea,#9fb0c6 55%,#c9cfd6)}
.photo-b{background:linear-gradient(135deg,#b58d63,#e8e6e1 45%,#5a9bc5 75%,#a07a56)}
.photo-c{background:linear-gradient(135deg,#3a2b24,#8a6a55 45%,#d9d4cf 80%,#e6e3df)}
.date{position:absolute;left:-20px;top:140px;width:66px;text-align:center;color:var(--white);font-family:"Roboto",sans-serif}
.date .day{display:block;height:30px;line-height:30px;background:var(--gold);font-size:17px;font-weight:700}
.date .mon{display:block;height:28px;line-height:28px;background:#3b3b3b;font-size:12px;font-weight:700}
.post h3{font-size:19px;font-weight:500;color:var(--ink);margin-top:28px}
.post p{font-size:13px;line-height:22px;color:var(--muted);margin-top:10px}
.post-meta{border-top:2px solid #e6e6e6;margin-top:18px;padding-top:14px;font-size:12px;color:var(--muted);display:flex;gap:14px}
.post-meta span{display:flex;align-items:center;gap:6px}

/* calculator */
.calc{position:absolute;left:0;top:1834px;width:1200px;height:424px;overflow:hidden}
.calc-photo{position:absolute;inset:0;background:linear-gradient(100deg,#8d8d8d 30%,#5e5e5e 55%,#3a3a3a 75%,#8c7860 100%)}
.calc-shade{position:absolute;inset:0;background:rgba(0,0,0,.25)}
.calc-wedge{position:absolute;left:0;top:0}
.calc h2{position:absolute;left:98px;top:54px;width:400px;color:var(--white);font-size:30px;font-weight:500;line-height:42px}
.calc-copy{position:absolute;left:98px;top:150px;width:260px;font-size:13px;line-height:22px;color:var(--white)}
.read-more{position:absolute;left:98px;top:248px;font-size:13px;font-weight:700;color:var(--white)}
.calc-row{position:absolute;left:530px;width:570px;height:38px}
.calc-row label{position:absolute;left:0;top:0;font-size:13px;line-height:19px;color:var(--white);width:60px}
.track{position:absolute;left:68px;top:16px;width:262px;height:7px;border-radius:4px;background:#2d3a50}
.knob{position:absolute;top:-6px;width:18px;height:18px;border-radius:50%;background:var(--white)}
.calc-field{position:absolute;left:354px;top:0;width:216px;height:38px;background:var(--white);font-size:14px;color:var(--ink);padding-left:16px;line-height:38px}
.freq{position:absolute;left:530px;top:236px;display:flex;gap:38px;color:var(--white);font-size:14px}
.freq span{display:flex;align-items:center;gap:10px}
.radio{width:14px;height:14px;border-radius:50%;border:2px solid var(--white)}
.radio.on{background:radial-gradient(circle,var(--white) 30%,transparent 35%)}
.estimate{position:absolute;left:530px;top:278px;font-size:16px;font-weight:600;color:var(--white)}
.apply-calc{position:absolute;left:884px;top:326px;width:140px;height:40px;border-radius:20px;background:var(--gold);color:var(--white);font-size:14px;font-weight:700;display:flex;align-items:center;justify-content:center;gap:8px}

/* partners */
.partners-title{top:2332px}
.partners{position:absolute;left:98px;top:2402px;display:flex;gap:30px}
.partner{width:176px;height:86px;border:2px solid #e2e2e2;display:flex;align-items:center;justify-content:center}
.partner-badge{width:110px;height:30px;background:#cfcfcf;border-radius:3px}

/* footer */
.footer{position:absolute;left:0;top:2530px;width:1200px;height:470px;background:var(--footer);color:#d0d0d0}
.footer-curve{position:absolute;left:0;top:0}
.footer-brand{position:absolute;left:98px;top:210px;font-family:"Roboto",sans-serif;font-size:29px;font-weight:500;line-height:42px;color:var(--white)}
.footer h4{position:absolute;top:164px;font-size:15px;font-weight:700;color:var(--white);text-transform:uppercase}
.quick-links{position:absolute;left:354px;top:206px;list-style:none;font-size:12px;line-height:20px;color:var(--white)}
.news-copy{position:absolute;left:540px;top:206px;width:260px;font-size:13px;line-height:22px;color:var(--white)}
.news-field{position:absolute;left:540px;top:260px;width:254px;height:36px;background:var(--white);font-size:12px;color:#555;padding-left:12px;line-height:36px}
.news-btn{position:absolute;left:540px;top:314px;width:102px;height:32px;border-radius:16px;background:var(--gold);color:var(--white);font-size:11px;font-weight:700;text-align:center;line-height:32px}
.contact{position:absolute;left:880px;width:240px;font-size:12px;line-height:20px;color:var(--white);display:flex;gap:18px}
.contact svg{flex:none;margin-top:2px}
.footer-rule{position:absolute;left:98px;top:390px;width:1004px;height:1px;background:#3a3a3a}
.copyright{position:absolute;left:98px;top:416px;font-size:12px;color:var(--white)}
.social{position:absolute;left:974px;top:408px;display:flex;gap:12px}
.social span{width:26px;height:26px;border-radius:50%;border:1px solid #9a9a9a}
</style>
</head>
<body>

<header class="hero">
  <div class="hero-photo" role="img" aria-label="Photo of two business people shaking hands in front of a tall office building"></div>
  <div class="hero-shade"></div>
  <div class="brand"><span class="brand-mark"></span><span class="brand-name">Ferncastle Financial</span></div>
  <div class="topbar">
    <span><svg width="16" height="16" viewBox="0 0 24 24" fill="#c9a063"><path d="M6.6 10.8a15 15 0 006.6 6.6l2.2-2.2a1 1 0 011-.25 11.4 11.4 0 003.6.57 1 1 0 011 1V20a1 1 0 01-1 1A17 17 0 013 4a1 1 0 011-1h3.5a1 1 0 011 1c0 1.25.2 2.45.57 3.6a1 1 0 01-.25 1z"/></svg>CALL US : <span class="phone-num">1 800 555 0142</span></span>
    <span class="btn-outline apply-top"><svg width="13" height="13" viewBox="0 0 24 24" fill="#fff"><path d="M3 17.2V21h3.8L17.8 10l-3.8-3.8zM20.7 7a1 1 0 000-1.4l-2.3-2.3a1 1 0 00-1.4 0l-1.8 1.8 3.8 3.8z"/></svg>Apply Now</span>
  </div>
  <nav class="nav">
    <span class="active">Home</span><span>About Us</span><span>Borrower</span><span>Lenders</span><span>Resources</span><span>Contact</span>
    <svg width="16" height="16" viewBox="0 0 24 24" fill="none" stroke="#fff" stroke-width="3" style="margin-top:2px"><circle cx="10" cy="10" r="7"/><path d="M15 15l6 6"/></svg>
  </nav>
  <h1 class="hero-title">WELCOME TO FERNCASTLE FINANCIAL</h1>
  <p class="hero-sub">Providing access to hundreds of commercial real estate capital providers</p>
  <span class="btn-outline quote-btn">Get a Quote</span>
  <div class="dots"><span class="on"></span><span></span><span></span><span></span></div>
  <svg class="hero-curve" width="1200" height="100" viewBox="0 0 1200 100"><path d="M0 62 Q600 -10 1200 62 L1200 100 L0 100 Z" fill="#c9a063"/><path d="M0 72 Q600 2 1200 72 L1200 100 L0 100 Z" fill="#fff"/></svg>
</header>

<section class="services">
  <div class="service">
    <div class="service-icon"><svg width="40" height="44" viewBox="0 0 40 44" fill="#c9a063"><rect x="6" y="2" width="28" height="40" rx="2"/><g fill="#f2f2f2"><rect x="11" y="8" width="5" height="5"/><rect x="24" y="8" width="5" height="5"/><rect x="11" y="17" width="5" height="5"/><rect x="24" y="17" width="5" height="5"/><rect x="11" y="26" width="5" height="5"/><rect x="24" y="26" width="5" height="5"/><rect x="17" y="34" width="6" height="8"/></g></svg></div>
    <h3>Construction</h3>
    <p>Nemo enim ipsam voluptatequ ia volu ptas sit asperna</p>
  </div>
  <div class="service">
    <div class="service-icon"><svg width="44" height="44" viewBox="0 0 24 24" fill="#c9a063"><path d="M12 4V1L8 5l4 4V6a6 6 0 016 6 5.9 5.9 0 01-.7 2.8l1.5 1.5A8 8 0 0012 4zm0 14a6 6 0 01-6-6 5.9 5.9 0 01.7-2.8L5.2 7.7A8 8 0 0012 20v3l4-4-4-4z"/></svg></div>
    <h3>Bridge</h3>
    <p>Nemo enim ipsam voluptatequ ia volu ptas sit asperna</p>
  </div>
  <div class="service">
    <div class="service-icon"><svg width="44" height="44" viewBox="0 0 24 24"><circle cx="12" cy="12" r="11" fill="#c9a063"/><path d="M7 12.5l3.2 3.2L17 9" fill="none" stroke="#fff" stroke-width="2.6"/></svg></div>
    <h3>Permanent</h3>
    <p>Nemo enim ipsam voluptatequ ia volu ptas sit asperna</p>
  </div>
  <div class="service">
    <div class="service-icon"><svg width="48" height="42" viewBox="0 0 48 42" fill="none" stroke="#c9a063" stroke-width="3.5"><ellipse cx="19" cy="15" rx="16" ry="11"/><path d="M10 24l-4 8 10-5"/><path d="M36 14c6 2 9 6 9 10 0 3-2 6-5 8l2 7-8-5c-5 1-11-1-14-4"/></svg></div>
    <h3>Advisory</h3>
    <p>Nemo enim ipsam voluptatequ ia volu ptas sit asperna</p>
  </div>
</section>

<section class="logins">
  <div class="login login-client">
    <svg class="login-icon" width="94" height="86" viewBox="0 0 94 86" fill="#fff"><circle cx="47" cy="22" r="16"/><path d="M20 80c0-20 12-34 27-34s27 14 27 34z"/><circle cx="17" cy="30" r="11"/><path d="M0 74c0-14 7-24 17-24 4 0 7 1 10 3-5 6-8 13-8 21z"/><circle cx="77" cy="30" r="11"/><path d="M94 74c0-14-7-24-17-24-4 0-7 1-10 3 5 6 8 13 8 21z"/></svg>
    <h2 style="left:222px">CLIENT LOGIN</h2>
    <div class="field field-email" style="left:222px"><svg width="14" height="12" viewBox="0 0 14 12" fill="#999"><path d="M0 0h14v12H0zM1 1.5l6 4.5 6-4.5"/></svg>Email Address</div>
    <div class="field field-pass" style="left:222px"><svg width="11" height="13" viewBox="0 0 11 13" fill="#999"><rect y="5" width="11" height="8"/><path d="M2.5 5V3.5a3 3 0 016 0V5" fill="none" stroke="#999" stroke-width="1.6"/></svg>Password</div>
    <span class="btn-outline login-submit" style="left:222px">Submit</span>
    <span class="forgot" style="left:466px">Forgot Password?</span>
  </div>
  <div class="login login-lender">
    <svg class="login-icon" style="left:52px" width="66" height="76" viewBox="0 0 66 76" fill="#fff"><circle cx="33" cy="20" r="19"/><path d="M0 76c0-22 14-34 33-34s33 12 33 34z"/></svg>
    <h2 style="left:156px">LENDER LOGIN</h2>
    <div class="field field-email" style="left:156px"><svg width="14" height="12" viewBox="0 0 14 12" fill="#999"><path d="M0 0h14v12H0z"/></svg>Email Address</div>
    <div class="field field-pass" style="left:156px"><svg width="11" height="13" viewBox="0 0 11 13" fill="#999"><rect y="5" width="11" height="8"/><path d="M2.5 5V3.5a3 3 0 016 0V5" fill="none" stroke="#999" stroke-width="1.6"/></svg>Password</div>
    <span class="btn-outline login-submit" style="left:156px">Submit</span>
    <span class="forgot" style="left:400px">Forgot Password?</span>
  </div>
</section>

<h2 class="section-title blog-title">LATEST BLOG</h2>

<article class="post" style="left:98px">
  <div class="post-photo photo-a" role="img" aria-label="Photo of a smiling man working on a laptop in an office"></div>
  <div class="date"><span class="day">02</span><span class="mon">AUG</span></div>
  <h3>Finibus Bonorum et Malorum</h3>
  <p>Nam libero tempore, cum soluta nobis est eligendi optio cumque nihil impedit quo minus id qu..</p>
  <div class="post-meta"><span>&#9679; Alex Marin</span><span>&#9993; 3 Comments</span></div>
</article>
<article class="post" style="left:442px">
  <div class="post-photo photo-b" role="img" aria-label="Photo of financial charts, a calculator and a pen on a desk"></div>
  <div class="date"><span class="day">02</span><span class="mon">AUG</span></div>
  <h3>Finibus Bonorum et Malorum</h3>
  <p>Nam libero tempore, cum soluta nobis est eligendi optio cumque nihil impedit quo minus id qu..</p>
  <div class="post-meta"><span>&#9679; Alex Marin</span><span>&#9993; 3 Comments</span></div>
</article>
<article class="post" style="left:788px">
  <div class="post-photo photo-c" role="img" aria-label="Photo of hands using a calculator beside a laptop"></div>
  <div class="date"><span class="day">02</span><span class="mon">AUG</span></div>
  <h3>Finibus Bonorum et Malorum</h3>
  <p>Nam libero tempore, cum soluta nobis est eligendi optio cumque nihil impedit quo minus id qu..</p>
  <div class="post-meta"><span>&#9679; Alex Marin</span><span>&#9993; 3 Comments</span></div>
</article>

<section class="calc">
  <div class="calc-photo" role="img" aria-label="Photo of hands typing on a laptop keyboard"></div>
  <div class="calc-shade"></div>
  <svg class="calc-wedge" width="600" height="424" viewBox="0 0 600 424"><polygon points="0,0 572,0 196,424 0,228" fill="#c9a063"/></svg>
  <h2>HOW MUCH WOULD YOU LIKE TO BORROW?</h2>
  <p class="calc-copy">Nemo enim ipsam voluptatem quia volu ptas sit aspernatur aut odit aut fugit, sed quia consequuntur magni.</p>
  <span class="read-more">READ MORE &gt;&gt;</span>
  <div class="calc-row" style="top:64px"><label>Loan Amount</label><div class="track"><span class="knob" style="left:50px"></span></div><div class="calc-field">$20000</div></div>
  <div class="calc-row" style="top:118px"><label>Interest Rate</label><div class="track"><span class="knob" style="left:28px"></span></div><div class="calc-field">10%</div></div>
  <div class="calc-row" style="top:170px"><label>Loan Term</label><div class="track"><span class="knob" style="left:176px"></span></div><div class="calc-field">7 Years</div></div>
  <div class="freq"><span><i class="radio on"></i>Monthly</span><span><i class="radio"></i>Fortnightly</span><span><i class="radio"></i>Weekly</span></div>
  <div class="estimate">Your Estimated Repayments Would be:</div>
  <div class="calc-row" style="top:270px"><div class="calc-field">$73.98</div></div>
  <span class="apply-calc"><svg width="12" height="12" viewBox="0 0 24 24" fill="#fff"><path d="M3 17.2V21h3.8L17.8 10l-3.8-3.8zM20.7 7a1 1 0 000-1.4l-2.3-2.3a1 1 0 00-1.4 0l-1.8 1.8 3.8 3.8z"/></svg>APPLY NOW</span>
</section>

<h2 class="section-title partners-title">OUR PARTNERS</h2>
<div class="partners">
  <div class="partner"><span class="partner-badge"></span></div>
  <div class="partner"><span class="partner-badge"></span></div>
  <div class="partner"><span class="partner-badge"></span></div>
  <div class="partner"><span class="partner-badge"></span></div>
  <div class="partner"><span class="partner-badge"></span></div>
</div>

<footer class="footer">
  <svg class="footer-curve" width="1200" height="100" viewBox="0 0 1200 100"><path d="M0 0 H1200 V10 Q600 110 0 10 Z" fill="#c9a063"/><path d="M0 0 H1200 V0 Q600 96 0 0 Z" fill="#fff"/></svg>
  <div class="footer-brand">FERNCASTLE<br>FINANCIAL</div>
  <h4 style="left:354px">Quick Links</h4>
  <ul class="quick-links"><li>Home</li><li>About Us</li><li>Marketplace</li><li>Broker</li><li>Lenders</li><li>Resources</li><li>Blog</li><li>Contact</li></ul>
  <h4 style="left:540px">Newsletter Subscription</h4>
  <p class="news-copy">Register your Email Address to get information about us</p>
  <div class="news-field">Email Address</div>
  <div class="news-btn">SUBSCRIBE</div>
  <h4 style="left:880px">Contact Us</h4>
  <div class="contact" style="top:212px"><svg width="10" height="14" viewBox="0 0 10 14" fill="#fff"><path d="M5 0a5 5 0 015 5c0 4-5 9-5 9S0 9 0 5a5 5 0 015-5z"/><circle cx="5" cy="5" r="2" fill="#1f1f1f"/></svg><span>Meerweg 12, 4600 AB Verdam<br>Nederland</span></div>
  <div class="contact" style="top:276px"><svg width="12" height="12" viewBox="0 0 24 24" fill="#fff"><path d="M6.6 10.8a15 15 0 006.6 6.6l2.2-2.2a1 1 0 011-.25 11.4 11.4 0 003.6.57 1 1 0 011 1V20a1 1 0 01-1 1A17 17 0 013 4a1 1 0 011-1h3.5a1 1 0 011 1c0 1.25.2 2.45.57 3.6a1 1 0 01-.25 1z"/></svg><span>1 800 555 0142</span></div>
  <div class="contact" style="top:320px"><svg width="12" height="10" viewBox="0 0 14 12" fill="#fff"><path d="M0 0h14v12H0z"/></svg><span>info@ferncastlefinancial.com</span></div>
  <div class="footer-rule"></div>
  <div class="copyright">Copyrights &copy; 2017, Ferncastle Financial. All rights reserved.</div>
  <div class="social"><span></span><span></span><span></span><span></span></div>
</footer>

</body>
</html>
```